Telecom company needs marketing flyers

We need 3 different flyers to describe our product and how to qualify for the program. This our website to use for the logo and color scheme https://www.brivolinkmobile.com, however do not use the mascot on the flyer.

Attached are examples of a competitors flyers.

```html
<!DOCTYPE html>
<html lang="en">
<head>
<meta charset="UTF-8">
<title>Brivolink Mobile Flyers</title>
<link href="https://fonts.googleapis.com/css2?family=Poppins:ital,wght@0,400;0,500;0,600;0,700;0,800;1,400;1,700&display=swap" rel="stylesheet">
<style>
  :root{
    --bg:#f0f0f0;
    --white:#ffffff;
    --teal:#2cb3ad;
    --sky:#1fa8dc;
    --navy:#1f57a4;
    --bright:#1ea3da;
    --ink:#111111;
  }
  *{margin:0;padding:0;box-sizing:border-box}
  html,body{width:1200px;height:989px;overflow:hidden;background:var(--bg);font-family:'Poppins',sans-serif}
  .canvas{position:relative;width:1200px;height:989px}
  .flyer{position:absolute;background:var(--white);overflow:hidden;box-shadow:2px 3px 6px rgba(0,0,0,.12)}
  .flyer--steps{left:54px;top:72px;width:524px;height:678px}
  .flyer--care{left:619px;top:226px;width:523px;height:677px}
  .abs{position:absolute}
  svg.shape{position:absolute;left:0;top:0}
  .brand{font-weight:600;letter-spacing:2px;font-size:17px;white-space:nowrap}
  .h-white{color:var(--white);font-weight:700;text-transform:uppercase;white-space:nowrap}

  /* steps flyer */
  .steps-brand{left:28px;top:40px;color:var(--white)}
  .steps-headline{left:28px;top:92px;font-size:16.5px;line-height:20.5px}
  .coverage{left:28px;top:292px;font-size:18.5px;line-height:23px;color:var(--navy);font-weight:700;white-space:nowrap}
  .follow{left:28px;top:369px;font-size:18.5px;line-height:23px;color:var(--bright);font-weight:700;white-space:nowrap}
  .step-list{left:28px;top:416px;list-style:none;font-size:13.3px;color:var(--ink);white-space:nowrap}
  .step-list li{height:20.5px;line-height:20.5px}
  .step-list b{color:var(--navy);display:inline-block;width:21px}
  .perks{left:349px;top:421px;font-size:15.5px;line-height:18.5px;color:var(--bright);font-weight:700;white-space:nowrap}
  .footer-band{left:0;top:524px;width:524px;height:90px;background:linear-gradient(90deg,var(--teal),var(--sky))}
  .call{left:28px;top:13px;color:var(--white);font-weight:700;white-space:nowrap}
  .call .label{font-size:18.5px;line-height:22px}
  .call .phone{font-size:20px;line-height:23px}
  .call .url{font-size:12px;line-height:16px}
  .review{left:286px;top:8px;width:212px;color:var(--white);font-size:9px;line-height:11.5px;font-style:italic}
  .review .who{font-weight:700}
  .review .quote{margin-top:11px;font-weight:400}

  /* care flyer */
  .care-box{left:265px;top:10px;width:258px;height:141px;background:linear-gradient(90deg,var(--teal),var(--sky));border-radius:22px 0 0 22px}
  .care-box-text{left:30px;top:11px;font-size:16.5px;line-height:20.5px}
  .care-box-text p+p{margin-top:20px}
  .intro{left:32px;top:286px;width:212px;font-size:11.3px;line-height:13.4px;font-weight:700;color:var(--ink)}
  .divider{left:32px;top:390px;width:88px;height:2px;background:var(--bright)}
  .checks{left:32px;top:413px;list-style:none;font-size:11.8px;line-height:13.4px;color:var(--ink);width:200px}
  .checks li{position:relative;padding-left:23px;margin-bottom:13px}
  .checks svg{position:absolute;left:0;top:3px}
  .care-brand{left:32px;top:622px;color:var(--navy)}
  .care-offer{left:290px;top:384px;color:var(--white);white-space:nowrap}
  .care-offer .lead{font-size:16.8px;line-height:20.5px;text-transform:uppercase;font-weight:400}
  .care-offer .bold{font-weight:700;text-transform:uppercase}
  .care-offer .cov{margin-top:14px;font-size:18px;line-height:23px}
  .care-offer .cnow{margin-top:10px;font-size:18px;line-height:21px}
  .care-offer .ph{font-size:19.5px;line-height:22px}
  .care-offer .url{font-size:12px;line-height:16px}
</style>
</head>
<body>
<div class="canvas">

  <section class="flyer flyer--steps">
    <svg class="shape" width="524" height="678" viewBox="0 0 524 678">
      <defs>
        <linearGradient id="tealA" x1="0" y1="0" x2="1" y2="0"><stop offset="0" stop-color="#2cb3ad"/><stop offset="1" stop-color="#22a9d4"/></linearGradient>
        <linearGradient id="warmPhoto" x1="0" y1="0" x2="1" y2="1"><stop offset="0" stop-color="#e9e4e0"/><stop offset=".6" stop-color="#d8c4c2"/><stop offset="1" stop-color="#b9b8c4"/></linearGradient>
      </defs>
      <path d="M323,0 L524,0 L524,203 L375,308 Q340,332 305,320 Q262,300 262,250 L323,0 Z" fill="url(#warmPhoto)" role="img" aria-label="Photo of a child lying on a bed using a tablet"/>
      <path d="M0,0 L323,0 L273,195 L230,228 Q180,268 140,266 Q110,264 85,240 L0,161 Z" fill="url(#tealA)"/>
    </svg>
    <div class="abs brand steps-brand">BRIVOLINK MOBILE</div>
    <div class="abs h-white steps-headline">Get your limited time deal<br>today! Free service and<br>internet with your tablet!</div>
    <div class="abs coverage">NATIONWIDE COVERAGE<br>FOR $0! LIMITED TIME ONLY!</div>
    <div class="abs follow">FOLLOW THESE SIMPLE STEPS<br>FAST, EASY &amp; FREE SERVICE</div>
    <ol class="abs step-list">
      <li><b>1.</b>Check coverage in your area</li>
      <li><b>2.</b>Get in touch with us</li>
      <li><b>3.</b>Pick Your Plan</li>
      <li><b>4.</b>Place Order, Active Your Plan, &amp; Enjoy!</li>
    </ol>
    <div class="abs perks">LOW PRICES WITH<br>HIGH QUALITY<br>SERVICE &amp; BEST IN<br>CLASS SUPPORT</div>
    <div class="abs footer-band">
      <div class="abs call">
        <div class="label">CALL NOW</div>
        <div class="phone">+800-555-0142</div>
        <div class="url">WWW.BRIVOLINKMOBILE.COM</div>
      </div>
      <div class="abs review">
        <div class="who">Marcus T. ★★★★★<br>Great customer service</div>
        <div class="quote">“The customer service at Brivolink Mobile has been exceptional. They helped me make the transition as smooth as possible.”</div>
      </div>
    </div>
  </section>

  <section class="flyer flyer--care">
    <svg class="shape" width="523" height="677" viewBox="0 0 523 677">
      <defs>
        <linearGradient id="coolPhoto" x1="0" y1="0" x2="1" y2="1"><stop offset="0" stop-color="#d5dde2"/><stop offset="1" stop-color="#b6c2c9"/></linearGradient>
        <linearGradient id="tealB" x1="0" y1="0" x2="1" y2="1"><stop offset="0" stop-color="#2cb3ad"/><stop offset="1" stop-color="#1fa8dc"/></linearGradient>
      </defs>
      <rect x="0" y="0" width="523" height="268" fill="url(#coolPhoto)" role="img" aria-label="Photo of a smiling woman holding a tablet"/>
      <path d="M478,268 L523,321 L523,677 L294,677 L236,480 Q222,415 275,388 L420,308 Z" fill="url(#tealB)"/>
      <rect x="342" y="180" width="138" height="185" rx="18" fill="#3fa6c8" opacity=".85" role="img" aria-label="Illustrated character holding a tablet"/>
    </svg>
    <div class="abs care-box">
      <div class="abs h-white care-box-text">
        <p>Best in customer<br>care at your service</p>
        <p>Learn why 100,000+<br>customers trust<br>Brivolink Mobile!</p>
      </div>
    </div>
    <p class="abs intro">We understand the importance of having great customer service. Our support specialists are here to help you at any time with your questions and needs! Discover how Brivolink Mobile can help keep you connected</p>
    <div class="abs divider"></div>
    <ul class="abs checks">
      <li><svg width="13" height="15" viewBox="0 0 13 15"><path d="M6.5 1 L12 3 V7.5 Q12 12 6.5 14 Q1 12 1 7.5 V3 Z" fill="none" stroke="#1f57a4" stroke-width="1.2"/><path d="M4 7.5 L6 9.5 L9.2 5.8" fill="none" stroke="#1ea3da" stroke-width="1.2"/></svg>Quick response time frames (typically under 2-3 minutes)</li>
      <li><svg width="13" height="15" viewBox="0 0 13 15"><path d="M6.5 1 L12 3 V7.5 Q12 12 6.5 14 Q1 12 1 7.5 V3 Z" fill="none" stroke="#1f57a4" stroke-width="1.2"/><path d="M4 7.5 L6 9.5 L9.2 5.8" fill="none" stroke="#1ea3da" stroke-width="1.2"/></svg>Easy to speak to our support specialists</li>
      <li><svg width="13" height="15" viewBox="0 0 13 15"><path d="M6.5 1 L12 3 V7.5 Q12 12 6.5 14 Q1 12 1 7.5 V3 Z" fill="none" stroke="#1f57a4" stroke-width="1.2"/><path d="M4 7.5 L6 9.5 L9.2 5.8" fill="none" stroke="#1ea3da" stroke-width="1.2"/></svg>Self-service options always available to you (videos, FAQs, chat feature)<br>LOW PRICE</li>
    </ul>
    <div class="abs brand care-brand">BRIVOLINK MOBILE</div>
    <div class="abs care-offer">
      <div class="lead">Get your limited time<br>deal today! Free service<br>and internet with your<br>tablet!</div>
      <div class="bold cov">Nationwide<br>coverage for $0!<br>Limited time only!</div>
      <div class="bold cnow">Call now</div>
      <div class="bold ph">+800-555-0142</div>
      <div class="bold url">WWW.BRIVOLINKMOBILE.COM</div>
    </div>
  </section>

</div>
</body>
</html>
```